Re-design of current business cards

We are updating our website with new colors and layout. Would like to re-design our business cards to co-ordinate. See attached pdf with new Brindlecraft website colors. We would also like to combine our 2 brands on the one business card. Attached is the new design for our Brindlecraft website, current business cards, which are one sided, brindlecraft logo in tiff, .ai for fonts. Brindlecraft logo font is Optimum, Quillmarsh website home page image, Quillmarsh brand statics for products which includes the logo for this brand.

Quillmarsh brand will stay the dark gray on the website. See attached statics for product and website home page.
Updates

The business cards will be 2 sided. Brindlecraft Brand on one side and Quillmarsh Brand on the other. The colors for Brindlecraft need to follow the color scheme of the brindlecraft website pdf I uploaded. The colors are a blue, lighter teal blue and white. Quillmarsh needs to follow the dark gray color on files uploaded

Target Market(s)

The trade and consumers

Industry/Entity Type

Home Furnishing

Contact Information for Business Card

We are updating our website with new colors and layout. Would like to re-design our business cards to co-ordinate. We would also like to combine our 2 brands onto 1 2 sided business cards.

Requirements
Must have
• Colors that match our new website, see attached image.
• RGB colors
• navy -#152842
• teal - 98aeb9
• The gray color used for Quillmarsh brands.
• ll logos and fonts should stay the same.

```html
<!DOCTYPE html>
<html lang="en">
<head>
<meta charset="utf-8">
<title>Brindlecraft &amp; Quillmarsh Business Card</title>
<link rel="stylesheet" href="https://fonts.googleapis.com/css2?family=Tenor+Sans&family=Bodoni+Moda:wght@400&family=Roboto+Condensed:wght@300&display=swap">
<style>
  :root {
    --navy: #152842;
    --teal: #98aeb9;
    --band: #c9d6de;
    --globe-tint: #dde4e8;
    --quill-gray: #58585a;
    --paper: #ffffff;
    --backdrop: #eaeaea;
    --soft-white: #f2f2f2;
  }
  * { margin: 0; padding: 0; box-sizing: border-box; }
  html, body {
    width: 1200px; height: 1165px; overflow: hidden;
    background: var(--backdrop);
  }
  .card {
    position: absolute; top: 412px; width: 510px; height: 318px; overflow: hidden;
  }
  .card--brindlecraft { left: 36px; background: var(--paper); font-family: "Tenor Sans", sans-serif; color: var(--navy); }
  .card--quillmarsh { left: 637px; width: 513px; background: var(--quill-gray); color: var(--soft-white); }

  .card__backdrop { position: absolute; inset: 0; }
  .address-band { position: absolute; left: 0; right: 0; top: 246px; bottom: 0; background: var(--band); opacity: .85; }

  .brand { position: absolute; top: 28px; right: 22px; width: 170px; text-align: center; }
  .brand__dot { width: 30px; height: 30px; border-radius: 50%; background: var(--teal); margin: 0 auto 6px; }
  .brand__name { font-size: 20px; letter-spacing: .5px; line-height: 1; }

  .holder { position: absolute; left: 27px; top: 80px; }
  .holder__name { font-size: 32px; font-weight: 400; letter-spacing: .5px; line-height: 1; }
  .holder__title { font-size: 13.5px; margin-top: 10px; letter-spacing: .2px; }

  .contact { position: absolute; left: 27px; top: 173px; font-size: 13px; line-height: 26px; }
  .contact__label { opacity: .9; }

  .address { position: absolute; left: 27px; top: 251px; font-size: 13px; line-height: 26px; letter-spacing: .6px; }
  .website { position: absolute; right: 22px; top: 268px; font-size: 22px; letter-spacing: .3px; }

  .quill-mark { position: absolute; left: 0; right: 0; top: 96px; text-align: center; }
  .quill-mark__name { font-family: "Bodoni Moda", serif; font-size: 50px; letter-spacing: 1px; line-height: 1; }
  .quill-mark__by { font-family: "Roboto Condensed", sans-serif; font-weight: 300; font-size: 12px; text-align: right; width: 340px; margin: 2px auto 0; }
  .tagline { position: absolute; left: 0; right: 0; top: 198px; text-align: center; font-family: "Roboto Condensed", sans-serif; font-weight: 300; font-size: 22px; }
</style>
</head>
<body>
  <section class="card card--brindlecraft">
    <svg class="card__backdrop" width="510" height="318" role="img" aria-label="Large faint circle decoration">
      <circle cx="180" cy="176" r="172" fill="var(--globe-tint)"/>
    </svg>
    <div class="address-band"></div>

    <div class="brand">
      <div class="brand__dot"></div>
      <div class="brand__name">BRINDLECRAFT</div>
    </div>

    <div class="holder">
      <h1 class="holder__name">Dana Whitlow</h1>
      <p class="holder__title">GRAPHICS / PHOTOGRAPHY DIRECTOR</p>
    </div>

    <div class="contact">
      <div><span class="contact__label">Phone</span> 555 014 2270</div>
      <div><span class="contact__label">Email</span> dwhitlow@brindlecraft.com</div>
      <div><span class="contact__label">Fax</span> 555 014 2291</div>
    </div>

    <div class="address">
      <div>PO BOX 412/1870 FERNDALE RD</div>
      <div>ASHBURY GAP, VIRGINIA 20917</div>
    </div>
    <div class="website">brindlecraft.com</div>
  </section>

  <section class="card card--quillmarsh">
    <div class="quill-mark">
      <div class="quill-mark__name">QUILLMARSH</div>
      <div class="quill-mark__by">by BRINDLECRAFT</div>
    </div>
    <p class="tagline">Bring quiet comfort to every room.</p>
  </section>
</body>
</html>
```